Non-profit organisation for street children in Indonesia

Lentera Bocah provides home, education, family and health care for street children and other underprivileged children in Indonesia.

We need an emotional catchy advertisement that will make people aware of the terrible living conditions of street children in Indonesia and the great work the Lentera Bocah Foundation is doing to help these children.

We have 1 photo available for this advertisement. A little girl laying in the streets. This photo can be used with a strong quote such as "Street children whose responsibility?" or "Safer out on streets than at home" or "This child doesn't have the right to have a childhood worth remembering?" or another strong quote. Be creative! It need to touch people!

See some similar advertisements of other non-profit organizations what we very much like:

http://7brightpix.example/wp-content/uploads/2011/07/boldposters41.jpg
http://7brightpix.example/wp-content/uploads/2011/07/affiches-nobles-motifs-058.jpg

Mission
To give every child in the world the opportunity to live a happy and healthy life free of poverty, exploitation, and violence.

Overview
Lentera Bocah Foundation is an independent non-governmental organisation founded in 2005 in the Netherlands and expanded to Indonesia in 2006. Our aim is to improve the lives of children and to protect their rights by providing education, accommodation, family care and medical and legal aid.

Description
Lentera Bocah (Light for Youngsters) Foundation serves homeless and impoverished children by offering them a new path in life. By providing them with the necessary shelter, education, and psychological support directed towards vocational training, mentorship, and micro-credit opportunities, it strives to enable their re-entery into the community as happy and self-sufficient adults.

Facts:
There are 70 million children in Indonesia, nearly 18 million are very poor and estimated 170,000 children live on the streets.

Pitch submissions need to be 960x696 pixels.

Files available 1 photo and logo
Updates

Reason: Dear Designers, We have decided to extend the deadline because we haven't received what we are after. Please make a design in the trend as the following two examples: http://7brightpix.example/wp-content/uploads/2011/07/boldposters41.jpg http://7brightpix.example/wp-content/uploads/2011/07/affiches-nobles-motifs-058.jpg We hope to receive a good design shortly! Thank you Kind regards Lentera Bocah

Target Market(s)

Everybody

Industry/Entity Type

Non-Profit

Requirements
Must have
• 1. A strong quote.
2. Website url: www.lenterabocah.org
3. Mission quote from Lentera Bocah:
Should not have
• To much text.

```html
<!DOCTYPE html>
<html lang="en">
<head>
<meta charset="utf-8">
<title>Street children — whose responsibility? | Lentera Bocah Foundation</title>
<link rel="stylesheet" href="https://fonts.googleapis.com/css2?family=Anton&family=Open+Sans:wght@800&display=swap">
<style>
  :root {
    --backdrop: #ececec;
    --poster-green: #1f8a2a;
    --poster-green-deep: #14701f;
    --gold-light: #ffe45a;
    --gold: #f5c400;
    --gold-deep: #d99a00;
    --map-tint: rgba(190, 225, 185, 0.35);
    --photo-dark: #2a1c12;
    --photo-warm: #6b4a30;
    --white: #ffffff;
  }
  * { margin: 0; padding: 0; box-sizing: border-box; }
  html, body {
    width: 1200px; height: 769px; overflow: hidden;
    background: var(--backdrop);
  }
  .poster {
    position: absolute; left: 362px; top: 48px;
    width: 476px; height: 672px;
    background: radial-gradient(ellipse at 50% 45%, var(--poster-green) 0%, var(--poster-green-deep) 100%);
    border-top: 5px solid var(--gold);
    border-bottom: 5px solid var(--gold);
    overflow: hidden;
  }
  .headline {
    position: absolute; left: 0; right: 0; top: 16px;
    text-align: center;
    font-family: "Anton", sans-serif;
    font-weight: 400;
    line-height: 1;
    white-space: nowrap;
    background: linear-gradient(180deg, var(--gold-light) 0%, var(--gold) 55%, var(--gold-deep) 100%);
    -webkit-background-clip: text; background-clip: text;
    color: transparent;
  }
  .headline__line1 { display: block; font-size: 68px; letter-spacing: 0.5px; }
  .headline__line2 { display: block; font-size: 49px; margin-top: 6px; letter-spacing: 0.2px; }
  .map-shade {
    position: absolute; left: 20px; top: 440px; width: 440px; height: 130px;
    background: radial-gradient(ellipse at 50% 50%, var(--map-tint) 0%, transparent 70%);
  }
  .question-mark {
    position: absolute; left: 0; top: 168px; width: 476px; height: 360px;
  }
  .donate-row {
    position: absolute; left: 88px; top: 538px;
    display: flex; align-items: center; gap: 12px;
  }
  .donate-word {
    font-family: "Anton", sans-serif; font-size: 74px; line-height: 1;
    background: linear-gradient(180deg, var(--gold-light) 0%, var(--gold) 55%, var(--gold-deep) 100%);
    -webkit-background-clip: text; background-clip: text;
    color: transparent;
  }
  .org-name {
    display: flex; align-items: center; gap: 8px;
    font-family: "Open Sans", sans-serif; font-weight: 800;
    font-size: 19px; line-height: 1.05; color: var(--white);
  }
  .org-name__dot {
    width: 24px; height: 24px; border-radius: 50%;
    background: var(--gold);
  }
  .donate-info {
    position: absolute; left: 0; right: 0; top: 622px;
    text-align: center;
    font-family: "Open Sans", sans-serif; font-weight: 800;
    font-size: 13.5px; line-height: 1.45; color: var(--white);
    white-space: nowrap;
  }
</style>
</head>
<body>
  <main class="poster">
    <h1 class="headline">
      <span class="headline__line1">Street children</span>
      <span class="headline__line2">whose responsibility</span>
    </h1>

    <div class="map-shade" role="img" aria-label="Faint map of the Indonesian archipelago"></div>

    <svg class="question-mark" viewBox="0 0 476 372" preserveAspectRatio="none" role="img" aria-label="Photograph of street children, one boy making a peace sign, framed in a large question mark">
      <defs>
        <linearGradient id="photo-tone" x1="0" y1="0" x2="1" y2="1">
          <stop offset="0" stop-color="var(--photo-dark)"/>
          <stop offset="0.55" stop-color="var(--photo-warm)"/>
          <stop offset="1" stop-color="var(--photo-dark)"/>
        </linearGradient>
      </defs>
      <path d="M10,235 L10,145 C10,55 120,5 240,5 C385,5 472,70 472,175 C472,270 395,300 315,322 C265,336 242,345 242,367 L92,367 L92,325 C92,270 140,250 215,228 C270,212 275,195 275,180 L275,120 C275,100 260,95 240,95 C220,95 205,105 205,125 L205,235 Z"
            fill="url(#photo-tone)" stroke="var(--gold)" stroke-width="5" stroke-linejoin="round"/>
    </svg>

    <div class="donate-row">
      <span class="donate-word">DONATE</span>
      <span class="org-name"><span class="org-name__dot"></span>Lentera<br>Bocah</span>
    </div>

    <p class="donate-info">
      Donate to GIRO 4827 t.a.v. Stichting Lentera Bocah<br>
      or financial adopt a child on www.lenterabocah.org
    </p>
  </main>
</body>
</html>
```